Creative, Colorful, Dynamic Infographic for Global Non-Profit

We are a global arts and education non-profit in need of an infographic that illustrates four key skills embedded in our work: Curiosity, Listening, Imagination, Postive Action.
We work primarily with educators, students, and artists who use the power of personal stories to build community and connection and to bridge divides.
Our new brand guidelines, logos, and fonts are here: https://stylekit.example/quillbridge-7
I've attached a mock-up of the graphic and the required text. (Note the attached design was created by a staff person, your final design does not need to be the same. The color scheme and text of the final design should match the brand guidelines above.)
The graphic will be used for both web and print media and should include the purple Quillbridge 7 logo (also attached).
Ideally the final design will delight audiences and spark interest in our work.

```html
<!DOCTYPE html>
<html lang="en">
<head>
<meta charset="utf-8">
<title>Quillbridge 7 — Four Skills</title>
<link rel="stylesheet" href="https://fonts.googleapis.com/css2?family=DM+Serif+Display&family=Libre+Franklin:wght@400&family=Montserrat:wght@400&display=swap">
<style>
  :root {
    --purple: #663591;
    --green: #50b58c;
    --blue: #2f69b2;
    --red: #ee4343;
    --white: #ffffff;
    --paper: #ffffff;
  }
  html, body {
    margin: 0;
    padding: 0;
    width: 1197px;
    height: 1200px;
    overflow: hidden;
    background: var(--paper);
  }
  .skills-cycle {
    display: block;
    width: 1197px;
    height: 1200px;
  }
  .skill-title {
    font-family: "DM Serif Display", Georgia, serif;
    font-size: 64px;
    fill: var(--white);
    text-anchor: middle;
  }
  .skill-text {
    font-family: "Libre Franklin", Arial, sans-serif;
    font-size: 29px;
    fill: var(--white);
    text-anchor: middle;
  }
  .link-text {
    font-family: "Montserrat", Arial, sans-serif;
    font-size: 20px;
    fill: var(--white);
    text-anchor: middle;
  }
  .brand-name {
    font-family: "Libre Franklin", Arial, sans-serif;
    font-size: 38px;
    fill: var(--white);
    text-anchor: middle;
  }
  .fill-purple { fill: var(--purple); }
  .fill-green  { fill: var(--green); }
  .fill-blue   { fill: var(--blue); }
  .fill-red    { fill: var(--red); }
</style>
</head>
<body>
<svg class="skills-cycle" viewBox="0 0 1500 1500" preserveAspectRatio="none" xmlns="http://www.w3.org/2000/svg" role="img" aria-label="Cycle of four skills: Curiosity, Listening, Imagination, Positive action">

  <!-- connecting arrows -->
  <path class="link-arrow fill-purple" d="M320,590 C322,700 325,790 325,850 L285,850 L403,945 L488,818 L437,822 C436,760 438,680 440,590 Z"/>
  <path class="link-arrow fill-blue" d="M600,1098 C700,1108 780,1110 832,1104 L825,1050 L952,1135 L858,1255 L852,1213 C780,1222 680,1222 580,1215 Z"/>
  <path class="link-arrow fill-red" d="M1078,912 C1078,820 1078,740 1076,684 L1030,685 L1113,557 L1233,650 L1196,657 C1200,740 1200,820 1197,912 Z"/>
  <path class="link-arrow fill-green" d="M912,328 C840,335 760,336 690,328 L693,282 L565,368 L660,485 L655,448 C740,452 830,453 906,448 Z"/>

  <!-- skill circles -->
  <g class="skill skill-curiosity">
    <circle class="fill-purple" cx="392" cy="395" r="214"/>
    <text class="skill-title" x="392" y="345">Curiosity</text>
    <text class="skill-text" x="392" y="409">Focus on how you can</text>
    <text class="skill-text" x="392" y="447">learn from another’s</text>
    <text class="skill-text" x="392" y="485">knowledge and</text>
    <text class="skill-text" x="392" y="523">experience</text>
  </g>

  <g class="skill skill-positive-action">
    <circle class="fill-green" cx="1117" cy="393" r="214"/>
    <text class="skill-title" x="1120" y="336">Positive</text>
    <text class="skill-title" x="1120" y="383">action</text>
    <text class="skill-text" x="1117" y="440">Show your words</text>
    <text class="skill-text" x="1120" y="478">and actions matter</text>
  </g>

  <g class="skill skill-listening">
    <circle class="fill-blue" cx="396" cy="1106" r="214"/>
    <text class="skill-title" x="399" y="1085">Listening</text>
    <text class="skill-text" x="399" y="1151">Seek to understand</text>
    <text class="skill-text" x="399" y="1189">before speaking</text>
  </g>

  <g class="skill skill-imagination">
    <circle class="fill-red" cx="1124" cy="1110" r="214"/>
    <text class="skill-title" x="1130" y="1085">Imagination</text>
    <text class="skill-text" x="1130" y="1151">Consider possibilities</text>
    <text class="skill-text" x="1133" y="1189">beyond what you know</text>
  </g>

  <!-- arrow captions -->
  <g class="link-caption">
    <text class="link-text" x="376" y="674">Your</text>
    <text class="link-text" x="377" y="700">curiosity</text>
    <text class="link-text" x="379" y="726">allows</text>
    <text class="link-text" x="380" y="752">you to</text>
    <text class="link-text" x="384" y="778">listen</text>
  </g>
  <g class="link-caption">
    <text class="link-text" x="749" y="1144">Your listening allows</text>
    <text class="link-text" x="749" y="1170">you to take in new</text>
    <text class="link-text" x="752" y="1196">information</text>
  </g>
  <g class="link-caption">
    <text class="link-text" x="1138" y="710">Your</text>
    <text class="link-text" x="1138" y="734">imagination</text>
    <text class="link-text" x="1139" y="759">can</text>
    <text class="link-text" x="1141" y="784">spark</text>
    <text class="link-text" x="1141" y="808">positive</text>
    <text class="link-text" x="1145" y="832">action</text>
  </g>
  <g class="link-caption">
    <text class="link-text" x="775" y="370">Your positive actions</text>
    <text class="link-text" x="775" y="397">lead to curiosity about what</text>
    <text class="link-text" x="779" y="424">else is possible</text>
  </g>

  <!-- brand mark -->
  <g class="brand">
    <circle class="fill-purple" cx="764" cy="764" r="128"/>
    <text class="brand-name" x="764" y="777">Quillbridge 7</text>
  </g>
</svg>
</body>
</html>
```